The billboard should communicate confidence, energy and approachability while maintaining a professional, premium feel. Rather than relying on a standard agent photograph, property collage or crowded list of services, we would like an original creative idea that makes people look twice. This could involve a fun visual, clever headline, striking colour contrast or an unexpected real estate theme. The concept should feel positive and contemporary, with enough personality to become recognisable throughout the local community.

The key message should appeal to homeowners who are thinking about selling, preparing to sell or simply curious about the value of their property. Copy must be short, clear and conversational, supported by a direct call to action. The agent’s name, phone number and company branding should remain highly visible without competing with the main idea.

The finished billboard will measure 8.0 metres wide by 2.08 metres high (1224px x 324px), so the composition must suit a long landscape format. All important text and imagery should remain comfortably within safe margins and be legible from a distance. The design should avoid small writing, unnecessary detail and visual clutter.

The goal is to create a billboard that feels different from every other real estate sign in the area—something engaging, confident and easy to remember. It should build strong brand awareness, generate conversations and encourage local property owners to contact the agent when they are ready to make their next move. The concept should be adaptable for future campaigns, helping establish a consistent, distinctive and trusted local brand presence.

Target Market(s)

ages 30+

Industry/Entity Type

Real Estate

Requirements
Must have
• call Wade and phone number 0417 63 28 05
Nice to have
• Nice bright and yellow.. Exciting and grabbing

```html
<!DOCTYPE html>
<html lang="en">
<head>
<meta charset="utf-8">
<title>Lorne Bexley – Appraisal Billboard</title>
<link rel="stylesheet" href="https://fonts.googleapis.com/css2?family=Archivo+Black&family=Arimo:wght@400&display=swap">
<style>
  :root {
    --stage: #e9ebee;
    --paper: #fbfaf7;
    --ink: #1f1f1f;
    --ink-soft: #3a3a3a;
    --yellow: #ffe500;
    --yellow-deep: #f6c400;
    --band: #2a2a2a;
    --white: #ffffff;
  }
  * { margin: 0; padding: 0; box-sizing: border-box; }
  html, body {
    width: 1200px; height: 1178px; overflow: hidden;
    background: var(--stage);
  }
  .billboard {
    position: absolute; left: 0; top: 439px;
    width: 1200px; height: 300px;
    background: var(--paper);
    overflow: hidden;
    font-family: "Archivo Black", "Arial Black", sans-serif;
    color: var(--ink);
  }
  .panel { position: absolute; inset: 0; }
  .message { position: absolute; left: 34px; top: 0; z-index: 2; }
  .eyebrow {
    position: absolute; top: 76px; left: 0; white-space: nowrap;
    font-size: 15px; letter-spacing: 5.2px;
  }
  .headline { position: absolute; top: 100px; left: 0; white-space: nowrap; line-height: 1; }
  .headline-top { display: block; font-size: 50px; letter-spacing: -0.5px; }
  .headline-bottom { display: block; font-size: 35px; margin-top: 5px; letter-spacing: -0.3px; }
  .highlight { background: var(--yellow); padding: 0 4px; }
  .subline {
    position: absolute; top: 202px; left: 0; white-space: nowrap;
    font-family: "Arimo", Arial, sans-serif; font-size: 16px; color: var(--ink-soft);
  }
  .scene-art {
    position: absolute; left: 900px; top: 51px; width: 300px; height: 139px;
    background: linear-gradient(180deg, rgba(246,196,0,0) 0%, var(--yellow-deep) 55%, #3a3218 100%);
  }
  .brand {
    position: absolute; right: 14px; top: 14px;
    display: flex; align-items: center; gap: 6px;
    font-size: 13px; color: var(--ink); white-space: nowrap;
  }
  .brand-square { width: 12px; height: 12px; background: var(--white); }
  .contact { position: absolute; left: 692px; top: 199px; white-space: nowrap; }
  .agent-name { font-size: 25px; color: var(--yellow); line-height: 1; }
  .agent-role { font-size: 11px; color: var(--white); letter-spacing: 2.4px; line-height: 1.1; margin-top: 3px; }
  .agent-phone {
    display: flex; align-items: center; gap: 5px;
    font-size: 27px; color: var(--white); line-height: 1; margin-top: 3px; letter-spacing: 1px;
  }
  .agent-phone svg { width: 18px; height: 18px; }
  .office { font-size: 11px; color: var(--yellow); letter-spacing: 1.4px; line-height: 1.1; margin-top: 4px; }
</style>
</head>
<body>
  <section class="billboard">
    <svg class="panel" width="1200" height="300" viewBox="0 0 1200 300" aria-hidden="true">
      <polygon points="700,0 1200,0 1200,300 650,300" fill="var(--yellow)"/>
      <polygon points="680,190 1200,190 1200,300 669,300" fill="var(--band)"/>
      <g stroke="var(--yellow)" stroke-width="2" fill="none" stroke-linecap="round">
        <line x1="668" y1="62" x2="668" y2="22"/>
        <polyline points="659,32 668,22 677,32"/>
      </g>
    </svg>

    <div class="message">
      <p class="eyebrow">THINKING OF SELLING?</p>
      <h1 class="headline">
        <span class="headline-top">READY TO DISCOVER</span>
        <span class="headline-bottom">WHAT YOUR HOME IS <span class="highlight">WORTH?</span></span>
      </h1>
      <p class="subline">Your local property experts — get a free, no-obligation appraisal today.</p>
    </div>

    <div class="scene-art" role="img" aria-label="Illustration of dark house silhouettes, a tree and a rising growth line on yellow"></div>

    <div class="brand">
      <span class="brand-square"></span>
      <span>LORNE BEXLEY</span>
    </div>

    <div class="contact">
      <p class="agent-name">CALL WADE</p>
      <p class="agent-role">SALES CONSULTANT</p>
      <p class="agent-phone">
        <svg viewBox="0 0 24 24" aria-hidden="true"><path fill="#ffffff" d="M6.6 10.8a15.1 15.1 0 0 0 6.6 6.6l2.2-2.2a1 1 0 0 1 1-.25 11.4 11.4 0 0 0 3.6.57 1 1 0 0 1 1 1V20a1 1 0 0 1-1 1A17 17 0 0 1 3 4a1 1 0 0 1 1-1h3.5a1 1 0 0 1 1 1c0 1.25.2 2.45.57 3.57a1 1 0 0 1-.25 1z"/></svg>
        <span>0417 63 28 05</span>
      </p>
      <p class="office">LORNE BEXLEY [YOUR SUBURB]</p>
    </div>
  </section>
</body>
</html>
```